Guarenteed! - Homepage Website Design - Coding not required- Winner to complete further pages

Hi all,

We're looking at redesigning our current website with a few adjustments to other pages but the main adjustments will be on the homepage which is what this design request is for. Please note : any of these ideas can be changed if you have something particularly different / special in mind etc.

P.S Coding is not required, just a design.

- Our website -

Our website is simply a price comparison website that allows customers to find companies within their area at the best price. The products available are mostly related to the vehicle trade and all refer to vinyl. This includes the likes of vehicle window tint, vehicle colour change vehicle wrap, vehicle signage as well as other cosmetic vinyl modifications. We allow the customer to search for their product within their chosen area and receive a list of companies who supply their product within that area. From here they can compare prices and view further details on the company.

- What we're looking to do -

We're looking first of all to adjust how the website homepage is displayed, this includes adding images and adjusting the colours that are explained below:

First of all, we look to spread out each of the 12 products (which can be seen on the website as it stands) and add an image to each of the products (all being spaced out as shown in our sketch)

We've been told the website looks too busy so we're thinking if we adjust the colours to more simplier neutral colours as well as the main focus of the website being on the 12 images, that would be great.

- Logo + Banner -

Logo to remain top left although banner may be removed / adjusted to make simplier.

- Colours -

Adjustments - Colours shades
We want the website to still look exciting but simplify the colours. Needs to be kept up to date with the colours / textures etc (bright colours to highlight keypoints)
We're still looking to use either blue or orange or maybe both to highlight these keypoints but the main website to be light colours and maybe even black on white background. The entire homepage can be adjusted colour wise if you feel it fits into your theme including menu bars, banners etc. The key is to get this right with being not too overpowering with the colours but still look interesting and up to date.

- 1 - 4 steps banner - (text may change)

This sits just under the logo and explains to the user how easy the website is to use and the steps they need to take. This may change to a 1 - 5 steps but we're looking to have this designed once the overall colours / theme of the website is sorted.

- 12 images - 4 x 3

This is the main focus of the website and will be the main focus of what the customer sees first of all. This will be where they select their product and then underneath, enter their postcode and distance they would like to search within. As explained further up, we have some of the product images available so if you can where possible add these to the design and then duplicate the images on those we currently don't have available.

- 12 Images -Titles -

These titles will be in this order from left to right and etc

- Colour Change Wrap
- Printed Vehicle Wrap
- Window Tint
- Headlight Tint
- Vehicle Signage
- Shop Signage
- Roof Vinyl Wrap
- Bonnet Vinyl Wrap
- Carbon Fibre Vinyl
- Stickerbomb Vinyl
- Clear Protective Vinyl
- Wheel Refurb

Text to be quite large, centered and with the o to the left of the title. Short titles like 'Window Tint' should fit on one line in the middle of the box where as titles such as ' Stickerbomb Vinyl Wrap' should have the 'Stickerbomb Vinyl' on the first line with the 'Wrap' on the line below. The background of this text is up to experient, might be worth just a simple colour or it might be worth using a bright blue or orange to keep in with the theme of the logo etc.

These will also have the circle tick box to the left of the title (as on the current website) where the customer clicks to select the product they have available.
We were also thinking that if when the customer ticks the circle on their selected box, the box is highlighted in some way to show this.

- Search Block -

This will appear under the 12 images and allows the customer to input their postcode and distance for the search criteria. Colours on this can of course be adjusted to keep in theme with the website.

- Under the 12 Images -

- Block underneath the 12 images and search block -

To the left will be some key bullet points about the website - maybe 4 or 5 with a green tick to the left of this. Background colour will probably be best to be a light colour, possibly grey.

Then to the right of this will appear 4 images, 2 before and 2 after when applying these products. Images to be used aren't fully decided on and we would like this stage of the design left to the end when the rest of the theme etc have been decided on.

Attached images are as follows :
- How the website looks as it stands
- The fold line on the website (obviously important)
- Our rough sketch of how we'd like the website homepage to look.
- We have 7 of the images ready that are all attached in this one file. Please duplicate the images on those that currently don't have the image available.

We will also be requesting a website developer to put this into action if our current designer falls through so please feel free to contact us if potentially interested.

The layout can change if you can think of something particular different / unique that works with this design. The main idea is to not only get the 12 products on view to the viewers but also the keypoints and before and after images.

Any questions, please ask away as we're bound to have forgotten a few things.

Thanks and good luck!

Hi all, keep the designs coming.

We haven't quite seen that extra special design we're after. As stated, we're after something fairly simple to suit the youth as well as the middle aged but we're also after something that bit special.

Colours to concentrate on are still and orange etc although feel free to use other colours if you have anything special in mind.

Please experience and we'll give you our honest feedback.

Many thanks all and good luck!

Hi all, this is a message to all the designers.

Some good designs coming in but we're still after that something special for the website design. Keep the designs coming and please feel free to experiment with the design colours, layout etc.

The basic principle of the website needs to remain regarding the 12 products, search within block and 4 steps all appearing on the homepage.

The 4 steps seems to work best when it's got text as well as some simple images next to this.

A variation with the product titles with how to display this, some designers have gone with a simple white background whereas others have gone with colours. Please experiment here and where possible, add a contract / texture to the colour. Please remember the product titles needs to be clear, centured and with the circle tick box to the left of it. 

We're after a fairly simple design although we need it to look 21st century, up to date as well as interesting. The key points straight away are the 4 steps as well as the 12 products so try to guide the viewer to these areas a little.

White background behind the 12 images seems to be a much, although a light colour could possibly work.

The keypoints underneath these 12 products are too very important as it outlines what we do etc. Tick colour can vary.

Next to these keypoints will be the 'before' and 'after' images, these images needs to be fairly small and ensure there is white background around the image itself.

Good luck all and any questions, feel free to ask away.

Thanks!

Hi,

 Thank you for your time and effort with these designs, we are very nearly there with the design but we've thought of something that may work for the homepage. A curved arrow from step 1 pointing to the products, this may or may not work but feel free to give it a go.

Many thanks,

Thank you to everyone for your time and efforts with the design. It's hugely appreciated so thank you all once again.

Wish you all the luck in the future.

Trade

Serif
Sans Serif

```html
<!DOCTYPE html>
<html lang="en">
<head>
<meta charset="utf-8">
<title>Wrapscout — Find and Compare Vinyl Installers</title>
<link href="https://fonts.googleapis.com/css2?family=Signika:wght@300;400;600;700&family=Oswald:wght@500;600&display=swap" rel="stylesheet">
<style>
:root{
  --orange:#f08a1c;
  --orange-light:#f7a73f;
  --navy:#3b4a86;
  --navy-dark:#2c3768;
  --teal:#2a9fb7;
  --green:#3aa41c;
  --green-dark:#2a7d10;
  --page:#f2f2f2;
  --steps-bg:#f8f8f8;
  --tile-bg:#ffffff;
  --dark:#3a3a3a;
  --darker:#2b2b2b;
}
*{box-sizing:border-box;margin:0;padding:0}
html,body{width:1069px;height:1200px;overflow:hidden}
body{position:relative;background:var(--page);font-family:"Signika",sans-serif;color:var(--navy)}
.header{position:absolute;left:0;top:0;width:1069px;height:96px;background:linear-gradient(180deg,var(--orange-light),var(--orange))}
.brand{position:absolute;left:180px;top:26px;display:flex;align-items:center;gap:10px}
.brand-mark{width:30px;height:30px;border-radius:50%;background:#fff}
.brand-name{font-family:"Signika",sans-serif;font-weight:700;font-size:34px;color:#fff;letter-spacing:1px}
.brand-tag{position:absolute;left:180px;top:64px;font-size:11px;color:#fff;font-weight:600;letter-spacing:.5px}
.header-map{position:absolute;left:620px;top:0;width:449px;height:96px;background:linear-gradient(90deg,#f3a03a,#c9a658 55%,#8f9f6a)}
.header-banner{position:absolute;left:660px;top:8px;width:230px;height:50px;background:var(--navy-dark);color:#fff;font-weight:700;font-size:17px;line-height:22px;text-align:center;padding-top:3px;border-radius:3px}
.header-sub{position:absolute;left:664px;top:66px;font-weight:700;font-style:italic;font-size:17px;color:#fff}
.header-sub b{color:var(--navy-dark)}
.steps{position:absolute;left:0;top:96px;width:1069px;height:238px;background:var(--steps-bg);border-bottom:1px solid #e4e4e4}
.step-label{position:absolute;width:150px;text-align:center;font-weight:600;font-size:12.5px;line-height:14px;color:var(--navy);top:174px;letter-spacing:-.3px}
.products-title{position:absolute;left:180px;top:372px;font-weight:700;font-size:30px;color:var(--navy);letter-spacing:-.8px}
.products-rule{position:absolute;left:180px;top:406px;width:270px;border-top:2px dotted #b8bfd6}
.grid{position:absolute;left:179px;top:437px;display:grid;grid-template-columns:repeat(4,171px);grid-auto-rows:139px;column-gap:9px;row-gap:9px}
.tile{position:relative;background:var(--tile-bg);border:1px solid #ddd;box-shadow:0 1px 2px rgba(0,0,0,.08)}
.tile-photo{height:110px}
.tile-label{height:27px;display:flex;align-items:center;padding-left:9px;font-weight:600;font-size:13px;color:var(--navy);letter-spacing:-.4px}
.radio{width:11px;height:11px;border:1.5px solid var(--teal);border-radius:50%;margin-right:26px;flex:none;position:relative}
.is-selected .radio::after{content:"";position:absolute;left:2px;top:2px;width:4px;height:4px;border-radius:50%;background:var(--navy)}
.check{position:absolute;left:9px;top:9px;width:15px;height:15px;border-radius:50%;background:var(--orange)}
.search{position:absolute;left:179px;top:890px;width:713px;height:42px;border-radius:3px;background:linear-gradient(180deg,#55be2c,var(--green));border:1px solid var(--green-dark)}
.search-label{position:absolute;left:11px;top:8px;font-family:"Oswald",sans-serif;font-weight:600;font-size:19px;line-height:24px;color:#fff;letter-spacing:-1px;white-space:nowrap}
.search-field{position:absolute;top:8px;height:24px;background:#fff;border-radius:2px;font-size:10px;color:#aaa;padding:6px 14px}
.search-of{position:absolute;left:372px;top:6px;font-family:"Oswald",sans-serif;font-weight:600;font-size:22px;line-height:28px;color:#fff}
.search-btn{position:absolute;left:619px;top:8px;width:86px;height:25px;background:linear-gradient(180deg,#555,#2e2e2e);color:#fff;font-weight:600;font-size:14px;text-align:center;line-height:25px;border-radius:2px}
.about{position:absolute;left:0;top:952px;width:1069px;height:204px;background:var(--dark)}
.about-title{position:absolute;left:177px;top:26px;font-weight:700;font-size:23px;color:#fff;letter-spacing:-.8px}
.about-title span{color:var(--orange)}
.about-rule{position:absolute;left:177px;top:56px;width:355px;border-top:2px dotted #666}
.points{position:absolute;left:177px;top:70px;list-style:none}
.points li{display:flex;align-items:center;gap:12px;height:28.5px;font-weight:300;font-size:14.5px;color:#e8e8e8;letter-spacing:-.6px}
.gallery{position:absolute;left:615px;top:27px;display:grid;grid-template-columns:130px 130px;column-gap:14px;row-gap:8px}
.shot{position:relative;height:72px;background:#fff;padding:4px}
.shot-photo{width:100%;height:100%}
.shot-tag{position:absolute;left:-6px;top:-2px;padding:1px 8px;font-size:11px;font-weight:600;color:#fff}
.tag-before{background:var(--orange)}
.tag-after{background:var(--green)}
.footer{position:absolute;left:0;top:1156px;width:1069px;height:44px;background:var(--darker);font-size:9px;color:#aaa;font-weight:300}
.footer-links{position:absolute;left:180px;top:18px}
.footer-copy{position:absolute;right:177px;top:18px}
</style>
</head>
<body>

<header class="header">
  <div class="brand"><span class="brand-mark"></span><span class="brand-name">WRAPSCOUT</span></div>
  <div class="brand-tag">Find and Compare Vinyl Installers</div>
  <div class="header-map" role="img" aria-label="Map of England with installer location pins"></div>
  <div class="header-banner">FIND A PROFESSIONAL<br>VINYL INSTALLER TODAY</div>
  <div class="header-sub">Search &amp; Save in <b>Seconds!</b></div>
</header>

<section class="steps">
  <svg width="1069" height="170" viewBox="0 0 1069 170" style="position:absolute;left:0;top:0">
    <polygon points="178,80 892,80 878,100 892,120 178,120 192,100" fill="#f08a1c"/>
    <g>
      <circle cx="302" cy="98" r="44" fill="#3b4a86"/><path d="M286,136 L302,160 L318,136Z" fill="#3b4a86"/><circle cx="302" cy="98" r="35" fill="#fff"/>
      <circle cx="458" cy="98" r="44" fill="#3b4a86"/><path d="M442,136 L458,160 L474,136Z" fill="#3b4a86"/><circle cx="458" cy="98" r="35" fill="#fff"/>
      <circle cx="614" cy="98" r="44" fill="#3b4a86"/><path d="M598,136 L614,160 L630,136Z" fill="#3b4a86"/><circle cx="614" cy="98" r="35" fill="#fff"/>
      <circle cx="770" cy="98" r="44" fill="#3b4a86"/><path d="M754,136 L770,160 L786,136Z" fill="#3b4a86"/><circle cx="770" cy="98" r="35" fill="#fff"/>
    </g>
    <rect x="285" y="82" width="34" height="26" rx="2" fill="none" stroke="#f08a1c" stroke-width="4"/>
    <rect x="297" y="92" width="10" height="22" rx="4" fill="#3a3a3a"/>
    <rect x="440" y="84" width="36" height="28" fill="#3a3a3a"/><rect x="444" y="92" width="28" height="16" fill="#fff"/><rect x="446" y="96" width="14" height="3" fill="#f08a1c"/><rect x="446" y="101" width="18" height="3" fill="#f08a1c"/>
    <circle cx="618" cy="92" r="10" fill="none" stroke="#f08a1c" stroke-width="3"/><text x="618" y="97" text-anchor="middle" font-family="Signika,sans-serif" font-weight="700" font-size="13" fill="#f08a1c">$</text><rect x="600" y="104" width="16" height="12" fill="#3a3a3a"/>
    <rect x="756" y="84" width="10" height="32" rx="3" fill="#3a3a3a"/><path d="M768,98 L792,98 L792,114 L768,114Z" fill="#3a3a3a"/><path d="M768,98 L780,108 L792,98" fill="none" stroke="#fff" stroke-width="2"/>
    <g font-family="Signika,sans-serif" font-weight="700" font-size="16" fill="#fff" text-anchor="middle">
      <circle cx="264" cy="62" r="14" fill="#f08a1c"/><text x="264" y="68">1</text>
      <circle cx="420" cy="62" r="14" fill="#f08a1c"/><text x="420" y="68">2</text>
      <circle cx="575" cy="62" r="14" fill="#f08a1c"/><text x="575" y="68">3</text>
      <circle cx="731" cy="62" r="14" fill="#f08a1c"/><text x="731" y="68">4</text>
    </g>
  </svg>
  <div class="step-label" style="left:227px">SELECT CHOSEN<br>PRODUCT</div>
  <div class="step-label" style="left:383px">INPUT POSTCOD<br>+<br>SEARCH</div>
  <div class="step-label" style="left:542px">COMPARE COMPANIES<br>+<br>PRICES</div>
  <div class="step-label" style="left:694px">CONTACT CHOSEN<br>COMPANY</div>
</section>

<h1 class="products-title">Select Your Product</h1>
<svg width="28" height="34" viewBox="0 0 28 34" style="position:absolute;left:438px;top:376px">
  <path d="M4,6 C18,4 24,14 16,26" fill="none" stroke="#f08a1c" stroke-width="5" stroke-linecap="round"/>
  <path d="M9,22 L16,32 L22,21Z" fill="#f08a1c"/>
</svg>
<div class="products-rule"></div>

<main class="grid">
  <div class="tile is-selected"><div class="tile-photo" role="img" aria-label="White SUV with colour wrap" style="background:linear-gradient(180deg,#5b7a45,#b9b9b0)"></div><span class="check"></span><div class="tile-label"><span class="radio"></span>COLOUR WRAP</div></div>
  <div class="tile is-selected"><div class="tile-photo" role="img" aria-label="Van with printed livery wrap" style="background:linear-gradient(180deg,#eeeeee,#cfd7dc)"></div><span class="check"></span><div class="tile-label"><span class="radio"></span>PRINTED WRAP</div></div>
  <div class="tile"><div class="tile-photo" role="img" aria-label="Green hatchbacks with tinted windows" style="background:linear-gradient(135deg,#2f4a4a,#4fae3a)"></div><div class="tile-label"><span class="radio"></span>WINDOW TINT</div></div>
  <div class="tile"><div class="tile-photo" role="img" aria-label="Van with sign-written livery" style="background:linear-gradient(180deg,#6f7a6a,#d7d9d6)"></div><div class="tile-label"><span class="radio"></span>VEHICLE SIGNAGE</div></div>

  <div class="tile"><div class="tile-photo" role="img" aria-label="Office glass window signage" style="background:linear-gradient(180deg,#c9a770,#6a5a44)"></div><div class="tile-label"><span class="radio"></span>SHOP SIGNAGE</div></div>
  <div class="tile"><div class="tile-photo" role="img" aria-label="White car with black roof wrap" style="background:linear-gradient(180deg,#5a5a5a,#dedede)"></div><div class="tile-label"><span class="radio"></span>ROOF WRAP</div></div>
  <div class="tile"><div class="tile-photo" role="img" aria-label="White car with black bonnet wrap" style="background:linear-gradient(180deg,#4a4a4a,#e5e5e5)"></div><div class="tile-label"><span class="radio"></span>BONNET WRAP</div></div>
  <div class="tile"><div class="tile-photo" role="img" aria-label="Carbon fibre vinyl on car front" style="background:linear-gradient(180deg,#5d646c,#2d3238)"></div><div class="tile-label"><span class="radio"></span>CARBON FIBRE</div></div>

  <div class="tile"><div class="tile-photo" role="img" aria-label="Car with stickerbomb bonnet" style="background:linear-gradient(180deg,#e6e6e6,#c88a4a)"></div><div class="tile-label"><span class="radio"></span>STICKERBOMB</div></div>
  <div class="tile"><div class="tile-photo" role="img" aria-label="Clear protective film applied to car panel" style="background:linear-gradient(180deg,#d5d7da,#9a9ea3)"></div><div class="tile-label"><span class="radio"></span>CLEAR PROTECTIVE</div></div>
  <div class="tile"><div class="tile-photo" role="img" aria-label="Car front with tinted headlights" style="background:linear-gradient(180deg,#b49a60,#c9c9c9)"></div><div class="tile-label"><span class="radio"></span>HEADLIGHT TINT</div></div>
  <div class="tile"><div class="tile-photo" role="img" aria-label="Refurbished alloy wheel" style="background:linear-gradient(135deg,#3a3a3a,#a8a8a8)"></div><div class="tile-label"><span class="radio"></span>WHEEL REFURB</div></div>
</main>

<form class="search">
  <span class="search-label">SEARCH WITH IN :</span>
  <div class="search-field" style="left:151px;width:210px">10 MILES</div>
  <span class="search-of">OF</span>
  <div class="search-field" style="left:401px;width:210px">Eastbrook, Northshire</div>
  <div class="search-btn">SEARCH</div>
</form>

<section class="about">
  <h2 class="about-title">ABOUT <span>WRAPSCOUT</span></h2>
  <div class="about-rule"></div>
  <ul class="points">
    <li><svg width="20" height="16" viewBox="0 0 20 16"><path d="M2,8 L8,14 L18,2" fill="none" stroke="#3aa41c" stroke-width="4"/></svg>Dolor Sit Amet Consectetuer Adipiscing Diam Nonummy.</li>
    <li><svg width="20" height="16" viewBox="0 0 20 16"><path d="M2,8 L8,14 L18,2" fill="none" stroke="#3aa41c" stroke-width="4"/></svg>Nibh Euismod Tincidunt Ut Laoreet Dolore Magna</li>
    <li><svg width="20" height="16" viewBox="0 0 20 16"><path d="M2,8 L8,14 L18,2" fill="none" stroke="#3aa41c" stroke-width="4"/></svg>Consequat. Duis Autem Vel Eum Iriure Dolor In Hendrerit</li>
    <li><svg width="20" height="16" viewBox="0 0 20 16"><path d="M2,8 L8,14 L18,2" fill="none" stroke="#3aa41c" stroke-width="4"/></svg>Luptatum Zzril Delenit Augue Duis Dolore Te Feugait Nulla</li>
  </ul>
  <div class="gallery">
    <div class="shot"><div class="shot-photo" role="img" aria-label="SUV before wrap, white" style="background:linear-gradient(180deg,#9aa4a8,#e6e6e6)"></div><span class="shot-tag tag-before">Before</span></div>
    <div class="shot"><div class="shot-photo" role="img" aria-label="SUV after wrap, dark blue" style="background:linear-gradient(180deg,#8a9096,#3d4a66)"></div><span class="shot-tag tag-after">After</span></div>
    <div class="shot"><div class="shot-photo" role="img" aria-label="Saloon before wrap, yellow" style="background:linear-gradient(180deg,#4f6a3a,#d8c431)"></div><span class="shot-tag tag-before">Before</span></div>
    <div class="shot"><div class="shot-photo" role="img" aria-label="Saloon after wrap, lime green" style="background:linear-gradient(180deg,#4f6a3a,#a9d63a)"></div><span class="shot-tag tag-after">After</span></div>
  </div>
</section>

<footer class="footer">
  <div class="footer-links">ABOUT US | CONTACT US | FAQ | PRIVACY POLICY | TERMS &amp; CONDITIONS</div>
  <div class="footer-copy">COPYRIGHT WRAPSCOUT 2013. ALL RIGHTS RESERVED.</div>
</footer>

</body>
</html>
```